Wine labels Velmora Wine Council - Nueva etiqueta El Consejo Regulador de vinos de Albarrán

Velmora Wines Council, based in southern Spain, are looking to create a new suite of wine labels which retain the elegance of the Sherry Wines industry while reinvigorating their image to the modern era and a new generation of Sherry Wine lovers. These labels will be used across the Velmora Wines Council's range of wines for the promotion of the Sherry Wines industry.

Your design must present at least two styles of Sherry Wines which demonstrate an elegant, modern interpretation and understanding of the unique mood and personality for these wines and the essence of southern Spain.

10 labels will be created based on the winning design, one for each of the unique varieties of Sherry Wines within the collection. This collection comprises of several different wine varieties including: Fino, Manzanilla, Amontillado, Oloroso, Palo Cortado, Medium, Cream, Pale Cream, Pedro Ximenez and Moscatel.

We recommend you visit our website www.velmora-vinos.example/wines as the source to understanding the origins and unique personality of these diverse wines.

El Consejo Regulador de los Vinos de Albarrán y Tordesal quiere renovar las etiquetas de los vinos utilizados para sus actividades de promoción genérica. Esta colección de vinos comprende las tipologías más importantes de la región que incluye: fino, manzanilla, amontillado, oloroso, palo cortado, pale cream, medium, cream, pedro ximénez y moscatel. Por lo tanto se precisan 10 etiquetas, una para cada uno de los vinos mencionados.
Updates

Project Deadline Extended
Reason: Due to some confusion with the deadline we wish to officially extend the deadline to allow designers one last week to submit their entries.

Target Market(s)

Industry, journalists, media, sommeliers, chefs, wine writers

Industry/Entity Type

Council

Requirements
Must have
• Front and Back label plus capsule:
• Front label can have either of the two official logos of the Velmora Wine council titled Vinos de Albarrán Digital or not, this is optional. Must include: Vino selecionado por el Consejo Regulador de la Denominacion de Origen, Name of the variety of wine eg FINO, percentage of alcohol eg 15% and quantity 75 cl.
• The back of the label must include the council logo titled Sellora and 4 additional logos positioned smaller. The Europa logo must appear larger than the 3 other logos. Space for descriptive text about the wine is also required.
• The dimensions of the bottle can be found at this link http://www.vidrialto.example/es/catalogo/vinos-y-espumosos/bordelesas/bd-orla
• Altura:305 mm
• Diámetro base:76,20 mm
• Diámetro hombro:82 mm
• Tipo boca:Cetie
• Peso:750 gr
• Capacidad:75 cl
• Etiqueta delantera y trasera y capsula
• La etiqueta delantera puede incluir el logo oficial del Consejo Regulador o el logo digital, o ninguno, esto es opcional. Debe incluir el siguiete texto: Vino selecionado por el Consejo Regulador de la Denominacion de Origen, el nombre de la variedad del vino, por ejemplo Fino, el porcentaje de alcohol, por ejemplo 15%, y la capacidad 75cl.
• La etiqueta trasera debe incluir el logo oficial Sellora del Consejo, y cuatro logos adicionales con una dimension menor. El Logo de ¨Europa invierte en las zonas rurales¨ debe ser de mayor tamaño que los otros. Se precisa espacio para el texto descriptivo de los vinos.
• Las dimensiones de la botella se puede encontrar en este enlace
• http://www.vidrialto.example/es/catalogo/vinos-y-espumosos/bordelesas/bd-orla
• Altura:305 mm
• Diámetro base:76,20 mm
• Diámetro hombro:82 mm
• Tipo boca:Cetie
• Peso:750 gr
• Capacidad:75 cl
Nice to have
• See our website velmora-vinos.example to understand the origin of the wines. Ver nuestra página web velmora-vinos.example para mejor entender los vinos.
Should not have
• Images of catavinos or stereotypical images from Spain such as flamenco dancers or guitars.

```html
<!DOCTYPE html>
<html lang="es">
<head>
<meta charset="utf-8">
<title>Pedro Ximénez — etiqueta delantera</title>
<link rel="stylesheet" href="https://fonts.googleapis.com/css2?family=Playfair+Display:wght@800&family=Jost:wght@400&display=swap">
<style>
  :root {
    --paper: #ffffff;
    --ink: #111111;
    --ink-soft: #2b2b2b;
    --edge: #8a8a8a;
    --orange: #ff8000;
    --violet: #8000ff;
    --green: #22cc00;
  }
  html, body {
    margin: 0;
    padding: 0;
    overflow: hidden;
    background: var(--paper);
  }
  .label {
    position: relative;
    width: 672px;
    height: 1200px;
    background: var(--paper);
    border-left: 1px solid var(--edge);
    box-sizing: border-box;
    overflow: hidden;
  }
  .variety {
    position: absolute;
    top: 78px;
    left: 0;
    width: 672px;
    margin: 0;
    text-align: center;
    font-family: "Playfair Display", Georgia, serif;
    font-weight: 800;
    font-size: 84px;
    line-height: 78px;
    color: var(--ink);
    letter-spacing: 0.5px;
  }
  .variety span { display: block; }
  .variety .first { padding-left: 8px; }
  .legal {
    position: absolute;
    top: 259px;
    left: 78px;
    margin: 0;
    font-family: "Jost", "Futura", Arial, sans-serif;
    font-weight: 400;
    font-size: 19.5px;
    line-height: 20.5px;
    letter-spacing: 0.6px;
    color: var(--ink-soft);
    text-transform: uppercase;
  }
  .legal span { display: block; }
  .volume {
    position: absolute;
    top: 295px;
    left: 438px;
    margin: 0;
    font-family: "Jost", "Futura", Arial, sans-serif;
    font-weight: 400;
    font-size: 25px;
    line-height: 30px;
    color: var(--ink-soft);
  }
  .pattern-field {
    position: absolute;
    left: 0;
    top: 525px;
    width: 672px;
    height: 675px;
    background:
      radial-gradient(circle at 20% 25%, rgba(128,0,255,0.35), transparent 45%),
      radial-gradient(circle at 80% 70%, rgba(34,204,0,0.35), transparent 45%),
      linear-gradient(160deg, #ffb366 0%, #ff9a40 50%, #ffb366 100%);
  }
</style>
</head>
<body>
  <main class="label">
    <h1 class="variety"><span class="first">Pedro</span><span>Ximénez</span></h1>
    <p class="legal">
      <span>Vino selecionado por el</span>
      <span>Consejo Regulador de la</span>
      <span>Denominacion de origen</span>
    </p>
    <p class="volume">75cl 15%alc.</p>
    <div class="pattern-field" role="img" aria-label="Patrón geométrico repetido de círculos naranjas con centros violetas y verdes, y rectángulos inclinados violetas y verdes sobre líneas diagonales naranjas"></div>
  </main>
</body>
</html>
```